Defense contractor needs a roll-up for an exhibition

The booth we have booked has only a size of 3m².
So this will be the centerpiece of the whole booth.
We need a roll-up that attracts visitors and at the same time it should contain already designed graphics. These graphics are giving visitors an overview of our system. So it is necessary to have them exposed in a height that the booth personal can conveniently point with its fingers at them.
For information about our company and product visit:
https://www.brightlanternoptics.com/
For designing you should use Adobe Illustrator and the templates provided in the zip file, to guarantee a perfect print.
I have supplied my business card that you can copy the logo. As the company logo will be already at the booth nearby the top of the roll-up, you should not place it there. It can be in the middle or at the bottom.
I have uploaded a picture of the booth. The roll up will be placed at the left of the screen and has a size of 80cm x 200cm

Defense

Defense

Serif

Colors
0054AA
0677BA
7BADD7
CADEEF
E8F1F8

• you must use the Adobe Illustrator template to have a good printing result
• company logo on the upper side of the roll-up

```html
<!DOCTYPE html>
<html lang="en">
<head>
<meta charset="UTF-8">
<title>Bright Lantern Optics – Roll-up Banner</title>
<link rel="stylesheet" href="https://fonts.googleapis.com/css2?family=Oswald:wght@500;700&family=Montserrat:wght@300;500;600&display=swap">
<style>
  :root {
    --page: #f2f3f6;
    --paper: #ffffff;
    --ink: #141414;
    --sky: #0aa0e6;
    --sky-deep: #0a6fd8;
    --royal: #2a1fc8;
    --violet: #6a5ae0;
    --violet-soft: #c9c3f5;
    --photo-dark: #55594c;
    --photo-mid: #8f9283;
  }
  * { margin: 0; padding: 0; box-sizing: border-box; }
  html, body { width: 674px; height: 1200px; overflow: hidden; background: var(--page); }
  .rollup {
    position: absolute; left: 97px; top: 10px;
    width: 480px; height: 1180px;
    background: var(--paper);
    overflow: hidden;
    box-shadow: 0 6px 18px rgba(0,0,0,.22);
    font-family: "Montserrat", sans-serif;
    color: var(--ink);
  }
  .abs { position: absolute; }
  .brand-name {
    top: 60px; left: 0; width: 100%;
    text-align: center;
    font-family: "Oswald", sans-serif; font-weight: 700;
    font-size: 30px; letter-spacing: .5px; color: var(--ink);
  }
  .headline {
    top: 142px; left: 0; width: 100%;
    text-align: center;
    font-family: "Oswald", sans-serif; font-weight: 700;
    font-size: 47px; line-height: 52px; letter-spacing: .3px;
    background: linear-gradient(180deg, var(--sky) 0%, var(--sky-deep) 100%);
    -webkit-background-clip: text; background-clip: text; color: transparent;
  }
  .for-line {
    top: 256px; left: 0; width: 100%;
    display: flex; justify-content: center; align-items: center; gap: 18px;
    font-weight: 300; font-size: 32px; line-height: 40px;
  }
  .for-line .rule { width: 106px; height: 2px; background: var(--ink); }
  .subhead {
    top: 297px; left: 0; width: 100%;
    text-align: center; font-weight: 600;
    font-size: 31px; line-height: 39px; letter-spacing: 1px;
  }
  .art-scene {
    top: 280px; left: 0; width: 480px; height: 340px;
    background:
      radial-gradient(ellipse 22% 60% at 96% 55%, rgba(42,31,200,.75) 0%, rgba(42,31,200,0) 100%),
      radial-gradient(ellipse 55% 30% at 50% 78%, rgba(106,90,224,.6) 0%, rgba(106,90,224,0) 100%),
      linear-gradient(180deg, rgba(201,195,245,0) 62%, var(--violet-soft) 78%, rgba(255,255,255,0) 100%);
    z-index: 0;
  }
  .services-box {
    top: 547px; left: 31px; width: 424px; height: 104px;
    background: var(--sky); border-radius: 14px;
  }
  .services-tab {
    top: 537px; left: 140px; width: 201px; height: 35px;
    background: var(--royal); border-radius: 16px;
    color: #fff; font-weight: 500; font-size: 22px; letter-spacing: .5px;
    display: flex; align-items: center; justify-content: center;
  }
  .services-note {
    top: 579px; left: 40px; width: 406px;
    text-align: center; color: #fff; font-size: 13px; line-height: 18px;
  }
  .service { top: 622px; width: 110px; text-align: center; }
  .service svg { display: block; margin: 0 auto; }
  .service-label {
    margin-top: 2px;
    font-family: "Oswald", sans-serif; font-weight: 500;
    font-size: 16px; line-height: 20px; color: var(--ink);
    text-transform: uppercase;
  }
  .stripes { top: 0; left: 0; }
  .photo-soldier {
    top: 750px; left: 40px; width: 380px; height: 430px;
    background:
      radial-gradient(ellipse 50% 60% at 50% 55%, var(--photo-dark) 0%, var(--photo-mid) 55%, rgba(143,146,131,0) 100%);
  }
  .site-pill {
    top: 1110px; left: 40px; width: 400px; height: 43px;
    background: var(--royal); border-radius: 10px;
    color: #fff; font-weight: 600; font-size: 22px;
    display: flex; align-items: center; justify-content: center;
  }
</style>
</head>
<body>
<main class="rollup">
  <div class="abs art-scene" role="img" aria-label="Violet silhouettes of a helicopter, a tank, advancing soldiers and a standing soldier"></div>

  <div class="abs brand-name">BRIGHT LANTERN OPTICS</div>

  <h1 class="abs headline">ADVANCED COMBAT<br>TRAINING SYSTEMS</h1>

  <div class="abs for-line"><span class="rule"></span><span>FOR</span><span class="rule"></span></div>
  <h2 class="abs subhead">REALISTIC COMBAT<br>SIMULATION</h2>

  <section>
    <div class="abs services-box"></div>
    <div class="abs services-tab">SERVICES</div>
    <p class="abs services-note">The signature of the contract is not the end - it is just the beginning of a long-lasting partnership.</p>

    <div class="abs service" style="left:25px">
      <svg width="64" height="64" viewBox="0 0 64 64">
        <circle cx="32" cy="32" r="31" fill="var(--sky)"/>
        <circle cx="32" cy="32" r="26" fill="var(--royal)" stroke="#fff" stroke-width="2"/>
        <circle cx="32" cy="32" r="12" fill="none" stroke="#fff" stroke-width="2" stroke-dasharray="4 2"/>
        <path d="M26 32l4 4 8-8" fill="none" stroke="#fff" stroke-width="2.2" stroke-linecap="round"/>
      </svg>
      <div class="service-label">Extended<br>Warranty<br>Programs</div>
    </div>

    <div class="abs service" style="left:133px">
      <svg width="64" height="64" viewBox="0 0 64 64">
        <circle cx="32" cy="32" r="31" fill="var(--sky)"/>
        <circle cx="32" cy="32" r="26" fill="var(--royal)" stroke="#fff" stroke-width="2"/>
        <circle cx="32" cy="27" r="7" fill="none" stroke="#fff" stroke-width="2" stroke-dasharray="3 2"/>
        <circle cx="32" cy="27" r="2.5" fill="#fff"/>
        <path d="M20 40h8l4 3h10" fill="none" stroke="#fff" stroke-width="2" stroke-linecap="round"/>
      </svg>
      <div class="service-label">Logistics<br>Support</div>
    </div>

    <div class="abs service" style="left:244px">
      <svg width="64" height="64" viewBox="0 0 64 64">
        <circle cx="32" cy="32" r="31" fill="var(--sky)"/>
        <circle cx="32" cy="32" r="26" fill="var(--royal)" stroke="#fff" stroke-width="2"/>
        <path d="M22 42L40 24M24 22l18 18" fill="none" stroke="#fff" stroke-width="2.5" stroke-linecap="round"/>
        <circle cx="41" cy="23" r="4" fill="none" stroke="#fff" stroke-width="2"/>
      </svg>
      <div class="service-label">Maintenance<br>Contracts</div>
    </div>

    <div class="abs service" style="left:355px">
      <svg width="64" height="64" viewBox="0 0 64 64">
        <circle cx="32" cy="32" r="31" fill="var(--sky)"/>
        <circle cx="32" cy="32" r="26" fill="var(--royal)" stroke="#fff" stroke-width="2"/>
        <circle cx="28" cy="35" r="7" fill="none" stroke="#fff" stroke-width="2" stroke-dasharray="3 2"/>
        <circle cx="38" cy="26" r="5" fill="none" stroke="#fff" stroke-width="2" stroke-dasharray="3 2"/>
        <circle cx="28" cy="35" r="2" fill="#fff"/>
      </svg>
      <div class="service-label">Long-term<br>Spare Part<br>Services</div>
    </div>
  </section>

  <svg class="abs stripes" width="480" height="1180" viewBox="0 0 480 1180" aria-hidden="true">
    <polygon points="480,780 480,1180 70,1180" fill="var(--sky)"/>
    <polygon points="480,840 480,860 160,1180 140,1180" fill="#fff"/>
    <polygon points="480,1020 480,1036 336,1180 320,1180" fill="#fff"/>
    <polygon points="0,1150 40,1110 40,1128 0,1168" fill="var(--sky)"/>
  </svg>

  <div class="abs photo-soldier" role="img" aria-label="Photograph of a soldier in camouflage uniform and helmet holding a rifle"></div>

  <div class="abs site-pill">www.brightlanternoptics.com</div>
</main>
</body>
</html>
```